Modern business card for triathlon training business in Australia

We need a business card design for our triathlon training company.

Pace with Us Fitness is an Australian business, owned by women, run for women. Pace with Us Fitness helps women prepare or improve triathlon skills and confidence through triathlon camps completely designed for women.

Our camps focus on preparing women both physically and mentally for their next (or first!) triathlon.

You can see our website www.pacewithusfitness.com.au for more info about our business and our style.

We've attached two of our logos and are happy to consider a design that utilised either colour scheme with the teal colour being our 'feature' colour. We don't want overly feminine cards but rather cards that are professional and neat. If the inclusion of any pictures/art is warranted, this should be focused on our swim/ride/run theme and in that specific order (swim/ride/run).

The business card needs to be a printable design and the contact details will need to change for our two employees.

Target Market(s)

Female clients and partners/vendors/sponsors that we work with in the triathlon industry

Industry/Entity Type

Fitness

Contact Information for Business Card

Pace with Us Fitness (business name)
Nina Carver
Business Director
Mobile: 0438 916 207
Email: nina@pacewithusfitness.com.au
www.pacewithusfitness.com.au

Second business card:
Pace with Us Fitness
Bel Stray
Coaching Director
Mobile: 0459 260 718
Email: bel@pacewithusfitness.com.au

Font styles to use
Serif
Sans Serif

Requirements
Must have
• Core contact details above, our logo and be a printable design
Should not have
• Pink
• Cursive/script fonts

```html
<!DOCTYPE html>
<html lang="en">
<head>
<meta charset="utf-8">
<title>Pace with Us Fitness – Business Card</title>
<link rel="stylesheet" href="https://fonts.googleapis.com/css2?family=Open+Sans:wght@400;600;700&display=swap">
<style>
  :root {
    --teal: #0aa0bb;
    --teal-dark: #088ea6;
    --white: #ffffff;
    --paper: #f7f7f5;
    --grey: #8a9196;
    --ink: #4a4f53;
    --backdrop: #e9e9e6;
  }
  * { margin: 0; padding: 0; box-sizing: border-box; }
  html, body {
    width: 1200px; height: 768px; overflow: hidden;
    background: var(--backdrop);
    font-family: "Open Sans", Arial, sans-serif;
  }
  .canvas { position: relative; width: 1200px; height: 768px; }

  .card {
    position: absolute; top: 229px;
    width: 540px; height: 310px;
    overflow: hidden;
    box-shadow: 0 6px 18px rgba(0,0,0,0.18);
  }

  /* Front */
  .card-front { left: 40px; background: var(--teal); color: var(--white); }
  .front-brand {
    position: absolute; top: 108px; left: 0; width: 100%;
    text-align: center; font-weight: 700; font-size: 34px;
    letter-spacing: 0.5px; text-transform: uppercase;
  }
  .front-web {
    position: absolute; top: 196px; left: 0; width: 100%;
    display: flex; align-items: center; justify-content: center; gap: 16px;
    font-size: 13px; font-weight: 600;
  }
  .front-web .rule { width: 70px; height: 1px; background: rgba(255,255,255,0.7); }

  /* Back */
  .card-back { left: 620px; background: var(--paper); }
  .card-back svg.shape { position: absolute; inset: 0; }
  .back-brand {
    position: absolute; left: 34px; top: 112px; width: 250px;
    color: var(--teal); font-weight: 700; font-size: 26px;
    line-height: 1.15; text-transform: uppercase;
  }
  .holder { position: absolute; left: 370px; top: 74px; color: var(--white); }
  .holder-name { font-size: 19px; font-weight: 700; text-transform: uppercase; letter-spacing: 0.3px; }
  .holder-role { font-size: 12px; margin-top: 2px; }

  .contacts {
    position: absolute; left: 322px; top: 188px;
    list-style: none; color: var(--white); font-size: 12.5px;
  }
  .contacts li { display: flex; align-items: center; gap: 10px; height: 21px; }
  .contacts svg { width: 11px; height: 11px; flex: none; }
</style>
</head>
<body>
<main class="canvas">

  <section class="card card-front" aria-label="Card front">
    <div class="front-brand">Pace with Us Fitness</div>
    <div class="front-web">
      <span class="rule"></span>
      <span>www.pacewithusfitness.com.au</span>
      <span class="rule"></span>
    </div>
  </section>

  <section class="card card-back" aria-label="Card back">
    <svg class="shape" width="540" height="310" viewBox="0 0 540 310">
      <path d="M335 0 Q395 150 195 310 L540 310 L540 0 Z" fill="var(--teal)"/>
      <path d="M322 0 Q384 150 180 310" fill="none" stroke="var(--grey)" stroke-width="7"/>
    </svg>

    <div class="back-brand">Pace with Us<br>Fitness</div>

    <div class="holder">
      <div class="holder-name">Nina Carver</div>
      <div class="holder-role">Business Director</div>
    </div>

    <ul class="contacts">
      <li>
        <svg viewBox="0 0 12 12"><path d="M2 1h2.5l1 3-1.5 1a7 7 0 0 0 3 3l1-1.5 3 1V10a1 1 0 0 1-1 1A9 9 0 0 1 1 2a1 1 0 0 1 1-1z" fill="#fff"/></svg>
        <span>0438 916 207</span>
      </li>
      <li>
        <svg viewBox="0 0 12 12"><rect x="0.5" y="2" width="11" height="8" fill="#fff"/><path d="M0.5 2l5.5 4.5L11.5 2" fill="none" stroke="var(--teal)" stroke-width="1"/></svg>
        <span>nina@pacewithusfitness.com.au</span>
      </li>
      <li>
        <svg viewBox="0 0 12 12"><circle cx="6" cy="6" r="5.3" fill="none" stroke="#fff" stroke-width="1.2"/><ellipse cx="6" cy="6" rx="2.2" ry="5.3" fill="none" stroke="#fff" stroke-width="1"/><path d="M0.7 6h10.6" stroke="#fff" stroke-width="1"/></svg>
        <span>www.pacewithusfitness.com.au</span>
      </li>
    </ul>
  </section>

</main>
</body>
</html>
```